pharmacy/travel clinic business card design

We need a business card for our new business called Brenwick Travel Clinic and Pharmacy. Our primary focus is doing consultations for people before travelling internationally and providing vaccinations and prescriptions for them. While the business is considered a pharmacy, it has more the look and feel of a doctor's office. The design should communicate a professional and trustworthy feel. I have attached a copy of the logo we are going to be using.
Updates
Thanks for the submissions.  If you haven`t been eliminated you are one of the finalists.  Decision will likely be made tomorrow.

Target Market(s)
Customers, other health care professionals, travel agents
Industry/Entity Type
Clinic
Look and feel
Each slider illustrates characteristics of the customer's brand and the style your logo design should communicate.

```html
<!DOCTYPE html>
<html lang="en">
<head>
<meta charset="utf-8">
<title>Brenwick Travel Clinic and Pharmacy – Business Card</title>
<link href="https://fonts.googleapis.com/css2?family=Fira+Sans:wght@400;600;700&display=swap" rel="stylesheet">
<style>
  :root {
    --bg: #e9eaec;
    --card: #ffffff;
    --tint: #e6f0cf;
    --blue: #1f5fb5;
    --blue-light: #35b3ea;
    --blue-dark: #1b3f95;
    --green: #8cc63f;
    --green-light: #c6e46a;
    --grey: #8f8f95;
    --grey-light: #c5c5ca;
    --text: #3a3a3a;
  }
  * { box-sizing: border-box; margin: 0; padding: 0; }
  html, body { width: 1200px; height: 861px; overflow: hidden; }
  body {
    background: var(--bg);
    font-family: "Fira Sans", Arial, sans-serif;
    position: relative;
  }
  .card {
    position: absolute;
    top: 280px;
    width: 510px;
    height: 300px;
    background: var(--card);
    box-shadow: 0 6px 20px rgba(0,0,0,0.18);
    overflow: hidden;
  }
  .card--front { left: 60px; }
  .card--back { left: 630px; }

  .card__pattern {
    position: absolute;
    inset: 0;
    background: linear-gradient(180deg, #ffffff 0%, #f4f8ea 45%, var(--tint) 100%);
  }

  .strip {
    position: absolute;
    top: 0;
    bottom: 0;
    display: flex;
    flex-direction: column;
  }
  .strip--left { left: 0; width: 30px; }
  .strip--right { right: 0; width: 36px; }
  .strip__seg--blue-top { height: 62px; background: linear-gradient(180deg, var(--blue-light), var(--blue-dark)); }
  .strip__seg--grey { flex: 1; background: linear-gradient(90deg, var(--grey), var(--grey-light)); }
  .strip__seg--green-bottom { height: 52px; background: linear-gradient(180deg, var(--green), #6ea52c); }
  .strip__seg--green-top { height: 76px; background: linear-gradient(180deg, var(--green-light), var(--green)); }
  .strip__seg--blue-bottom { height: 70px; background: linear-gradient(180deg, var(--blue-dark), var(--blue-light)); }

  .brand {
    position: absolute;
    display: flex;
    align-items: center;
    gap: 8px;
    color: var(--green);
    font-weight: 600;
    line-height: 1.05;
  }
  .brand__dot {
    flex: none;
    border-radius: 50%;
    background: var(--blue-light);
  }
  .brand--small { top: 28px; left: 230px; font-size: 21px; }
  .brand--small .brand__dot { width: 18px; height: 18px; }
  .brand--large { top: 100px; left: 78px; font-size: 40px; }
  .brand--large .brand__dot { width: 30px; height: 30px; }

  .person { position: absolute; left: 50px; top: 120px; }
  .person__name {
    color: var(--blue);
    font-weight: 700;
    font-size: 26px;
    letter-spacing: 0.2px;
  }
  .person__role {
    color: var(--green);
    font-weight: 600;
    font-size: 13px;
    margin-top: 2px;
  }

  .contact {
    position: absolute;
    left: 50px;
    top: 190px;
    list-style: none;
  }
  .contact__item {
    display: flex;
    align-items: center;
    gap: 6px;
    font-size: 12px;
    color: var(--text);
    height: 21px;
  }
  .contact__icon { width: 13px; height: 13px; flex: none; }
</style>
</head>
<body>

<section class="card card--front" aria-label="Business card front">
  <div class="card__pattern" role="img" aria-label="Soft wavy line pattern fading into light green"></div>
  <div class="strip strip--left">
    <div class="strip__seg strip__seg--blue-top"></div>
    <div class="strip__seg strip__seg--grey"></div>
    <div class="strip__seg strip__seg--green-bottom"></div>
  </div>
  <div class="strip strip--right">
    <div class="strip__seg strip__seg--green-top"></div>
    <div class="strip__seg strip__seg--grey"></div>
    <div class="strip__seg strip__seg--blue-bottom"></div>
  </div>

  <div class="brand brand--small">
    <span class="brand__dot"></span>
    <span>Brenwick<br>Travel Clinic<br>and Pharmacy</span>
  </div>

  <div class="person">
    <h1 class="person__name">NAME SURNAME</h1>
    <p class="person__role">POSITION</p>
  </div>

  <ul class="contact">
    <li class="contact__item">
      <svg class="contact__icon" viewBox="0 0 14 14"><circle cx="7" cy="7" r="7" fill="#8cc63f"/><path d="M7 3a2.5 2.5 0 0 0-2.5 2.5C4.5 7.5 7 11 7 11s2.5-3.5 2.5-5.5A2.5 2.5 0 0 0 7 3z" fill="#fff"/></svg>
      #123 Lorem Ipsum Street, Dolor City
    </li>
    <li class="contact__item">
      <svg class="contact__icon" viewBox="0 0 14 14"><circle cx="7" cy="7" r="7" fill="#8cc63f"/><path d="M4.5 3.5l1.5 0 .8 2-1 .8a5 5 0 0 0 2 2l.8-1 2 .8v1.5c0 .5-.5 1-1 .9A6.5 6.5 0 0 1 3.6 4.4c-.1-.5.4-.9.9-.9z" fill="#fff"/></svg>
      123.456.7890
    </li>
    <li class="contact__item">
      <svg class="contact__icon" viewBox="0 0 14 14"><circle cx="7" cy="7" r="7" fill="#8cc63f"/><rect x="5" y="3" width="4" height="8" rx="0.8" fill="#fff"/></svg>
      123.456.7890
    </li>
    <li class="contact__item">
      <svg class="contact__icon" viewBox="0 0 14 14"><circle cx="7" cy="7" r="7" fill="#8cc63f"/><rect x="3.5" y="4.5" width="7" height="5" fill="#fff"/><path d="M3.5 4.5L7 7.3l3.5-2.8" fill="none" stroke="#8cc63f" stroke-width="0.8"/></svg>
      name@brenwicktcp.com
    </li>
    <li class="contact__item">
      <svg class="contact__icon" viewBox="0 0 14 14"><circle cx="7" cy="7" r="7" fill="#8cc63f"/><rect x="3.5" y="4" width="7" height="5.5" rx="0.6" fill="#fff"/><rect x="5.5" y="10" width="3" height="1" fill="#fff"/></svg>
      www.brenwicktcp.com
    </li>
  </ul>
</section>

<section class="card card--back" aria-label="Business card back">
  <div class="card__pattern" role="img" aria-label="Soft wavy line pattern fading into light green"></div>
  <div class="strip strip--left">
    <div class="strip__seg strip__seg--blue-top"></div>
    <div class="strip__seg strip__seg--grey"></div>
    <div class="strip__seg strip__seg--green-bottom"></div>
  </div>
  <div class="strip strip--right">
    <div class="strip__seg strip__seg--green-top"></div>
    <div class="strip__seg strip__seg--grey"></div>
    <div class="strip__seg strip__seg--blue-bottom"></div>
  </div>

  <div class="brand brand--large">
    <span class="brand__dot"></span>
    <span>Brenwick<br>Travel Clinic<br>and Pharmacy</span>
  </div>
</section>

</body>
</html>
```